Enhance the web site presence of Kolrith Global Limited

Upgrade the current web site www.kolrithpanel.com to share with the audience our current plan and future developments of our company. I have created a worksheet which shows all the pages that I like to have. The home page in English, Japanese and Chinese is hyperlinked to the various pages. Under the product, we should allow the user to select "single sided PCB or double sided PCB". The translation of the contents of the pages with Japanese is not complete but the English and Chinese are complete. You can download the briefing and photos in the dropbox files below;

https://www.sharelocker.net/sh/xk4trw92mpd3ab1/BBQm_Lp841zzPq2Rw7KtYnHjEa?dl=0

Target Market(s)

Electronic companies

Industry/Entity Type

Electronic

Coding

Coded - Design and coding required

Number of Pages Required

5+ page

Font styles to use
Sans Serif

Colors
00a990
0353a1
33b8a4

Requirements
Must have
• Get a sense of confidence on our company's integrity and capability to deliver the highest quality PCBs with the most competitive prices and best services. A sense of elegance is essential as we DON'T treat profits as the number one goal. Our number goal is to do the RIGHT things right. Having a mixture of our company photos will be appropriate.

```html
<!DOCTYPE html>
<html lang="en">
<head>
<meta charset="utf-8">
<title>Kolrith Global Limited – Printed Circuit Boards</title>
<link href="https://fonts.googleapis.com/css2?family=Montserrat:wght@500;600;700&family=Roboto:wght@300;400;500;700&display=swap" rel="stylesheet">
<style>
:root{
  --teal:#00a990;
  --teal-light:#33b8a4;
  --blue:#0353a1;
  --blue-deep:#023f7d;
  --ink:#333a40;
  --muted:#7a8088;
  --line:#e3e6ea;
  --soft:#f4f6f8;
  --footer:#2a2c2e;
  --footer-deep:#1f2123;
}
*{box-sizing:border-box;margin:0;padding:0}
html,body{width:1200px;height:4138px;overflow:hidden}
body{font-family:"Roboto",Arial,sans-serif;color:var(--ink);background:#fff;font-size:14px}
.wrap{width:940px;margin:0 auto;position:relative}
h2.section-title{font-family:"Montserrat",Arial,sans-serif;font-weight:700;font-size:30px;color:var(--blue)}
h2.section-title span{color:var(--teal)}
.divider{display:flex;align-items:center;gap:0;margin-top:10px}
.divider i{display:block;width:22px;height:2px;background:var(--blue)}
.divider b{display:block;width:4px;height:14px;background:var(--blue);margin:0 4px}
.center{text-align:center}
.center .divider{justify-content:center}

/* top bar */
.topbar{height:38px;background:var(--teal);color:#fff;font-size:12px}
.topbar .wrap{display:flex;justify-content:space-between;align-items:center;height:38px}

/* header */
.header{height:105px}
.header .wrap{display:flex;align-items:center;height:105px}
.brand{display:flex;align-items:center;gap:10px;font-family:"Montserrat",sans-serif;font-weight:700;font-size:30px;color:var(--blue);width:270px}
.brand .mark{width:22px;height:22px;background:var(--blue)}
.info{display:flex;align-items:center;gap:10px;font-size:11px;color:var(--muted);line-height:1.4;margin-right:40px}
.info svg{flex:none}
.btn{display:inline-block;background:var(--teal);color:#fff;font-weight:500;border-radius:3px;text-align:center}
.header .btn{margin-left:auto;padding:10px 24px;font-size:13px}
.nav{height:42px;border-top:1px solid var(--line);border-bottom:1px solid var(--line)}
.nav .wrap{display:flex;align-items:center;height:42px;gap:26px;font-size:12px;font-weight:500}
.nav .active{color:var(--blue);border-bottom:2px solid var(--blue);padding:12px 0}
.nav .phone{margin-left:auto;display:flex;gap:10px;align-items:center;font-size:18px;font-weight:700;color:var(--ink)}

/* hero */
.hero{height:388px;position:relative;background:linear-gradient(120deg,#9fb1a6 0%,#c9d3cb 35%,#6f8c7b 65%,#3a5a4a 100%)}
.hero-title{position:absolute;left:181px;top:12px;width:470px;background:rgba(255,255,255,.92);padding:22px 26px;font-family:"Montserrat",sans-serif;font-size:26px;font-weight:500;line-height:1.35;color:var(--ink)}
.hero-title strong{color:var(--blue)}
.hero-title em{font-style:normal;color:var(--teal);font-weight:700}
.appointment{position:absolute;left:764px;top:33px;width:350px;background:rgba(255,255,255,.95)}
.appointment h3{background:var(--teal);color:#fff;font-size:17px;font-weight:500;padding:12px 16px;display:flex;gap:10px;align-items:center}
.appointment form{padding:14px 16px 16px}
.field{border:1px solid var(--line);height:30px;margin-bottom:8px;font-size:10px;color:var(--muted);padding:9px 10px;background:#fff}
.field.area{height:76px}
.appointment .btn{width:230px;padding:8px 0;margin:4px 0 0;font-size:14px;border:0}

/* features */
.features{height:79px;background:var(--blue)}
.features .wrap{display:flex;justify-content:space-between;align-items:center;height:79px;color:#fff;font-size:14px}
.feature{display:flex;gap:12px;align-items:center}

/* who */
.who{height:605px;padding-top:66px}
.who .intro{width:540px;margin-top:28px;font-size:12px;line-height:1.6;color:var(--muted)}
.who .photo{position:absolute;left:582px;top:74px;width:358px;height:396px;background:linear-gradient(160deg,#d9dfe3,#8fa0ab 55%,#4c5f6b)}
.cards{display:grid;grid-template-columns:261px 261px;gap:12px;margin-top:28px}
.card{height:136px;padding:16px 14px;font-size:11px;line-height:1.55;border:1px solid var(--line);box-shadow:0 2px 6px rgba(0,0,0,.06)}
.card h4{font-size:15px;font-weight:500;margin-bottom:12px;color:var(--blue)}
.card.filled{background:var(--blue);color:#dfe9f5;border-color:var(--blue)}
.card.filled h4{color:#fff}

/* stats */
.stats{height:271px;background:linear-gradient(90deg,var(--blue),#0b6cc4 50%,var(--blue))}
.stats .wrap{display:flex;justify-content:space-around;padding-top:72px;color:#fff;text-align:center}
.stat b{display:block;font-size:24px;font-weight:700;margin-top:14px}
.stat span{display:block;font-size:12px;margin-top:10px;opacity:.85}

/* products */
.products{height:764px;padding-top:64px}
.tabs{display:flex;justify-content:center;gap:0;margin-top:74px;font-size:12px}
.tabs span{padding:6px 22px}
.tabs .on{color:var(--blue);border-bottom:2px solid var(--blue)}
.tabs .sep{width:1px;padding:0;background:var(--line)}
.product-head{margin:62px 0 0 16px;font-size:16px;font-weight:500}
.product-head + .rule{width:160px;height:2px;background:var(--teal);margin:8px 0 0 16px}
.product-desc{margin:18px 0 0 16px;font-size:11px;color:var(--muted);width:560px;line-height:1.6}
.tables{display:flex;gap:28px;margin:26px 0 0 86px}
table{border-collapse:collapse;font-size:12px;box-shadow:0 2px 8px rgba(0,0,0,.1)}
th{background:var(--blue);color:#fff;text-align:left;font-weight:500;padding:11px 14px}
td{padding:10px 14px;border-bottom:1px solid var(--line);background:#fff}
tr:nth-child(even) td{background:var(--soft)}
.products .btn{display:block;width:120px;margin:36px auto 0;padding:10px 0;font-size:13px}

/* testimonials */
.testimonials{height:465px;background:linear-gradient(135deg,#0a63b8,var(--blue) 55%,#0a71c9);color:#fff;padding-top:60px;text-align:center}
.testimonials h2.section-title{color:#fff}
.testimonials .divider i,.testimonials .divider b{background:#fff}
.avatars{display:flex;justify-content:center;gap:20px;margin-top:50px}
.avatar{width:86px;height:86px;border-radius:50%;border:3px solid #fff;background:linear-gradient(160deg,#d7c1ae,#8b6e5a)}
.quote{width:760px;margin:40px auto 0;font-size:12px;line-height:1.7;opacity:.9}
.who-said{margin-top:16px;font-size:15px}
.who-said small{font-size:11px;opacity:.8}
.dots{display:flex;justify-content:center;gap:6px;margin-top:14px}
.dots i{width:9px;height:9px;border-radius:50%;border:1px solid #fff}
.dots i:first-child{background:#fff}

/* news */
.news{height:633px;padding-top:64px}
.news-list{display:flex;gap:30px;margin-top:56px}
.post{width:270px;height:382px;border:1px solid var(--line);box-shadow:0 2px 6px rgba(0,0,0,.06)}
.post .img{height:178px;background:linear-gradient(150deg,#c5d1cc,#6f8a80 60%,#3f5a52)}
.post .body{padding:14px}
.post h4{font-size:14px;font-weight:500}
.post .meta{font-size:10px;color:var(--muted);margin-top:6px}
.post p{font-size:11px;color:var(--muted);line-height:1.6;margin-top:12px}
.post a{display:block;color:var(--teal);font-size:11px;font-weight:500;margin-top:20px;text-decoration:none}

/* partners */
.partners{height:191px;background:var(--soft);border-top:1px solid var(--line)}
.partners .wrap{display:flex;align-items:center;justify-content:space-between;height:191px;width:1000px}
.partner{width:130px;height:84px;background:#fff;border:1px solid var(--line);display:flex;align-items:center;justify-content:center;font-family:"Montserrat",sans-serif;font-weight:700;font-size:16px;color:var(--blue)}

/* cta */
.cta{height:191px;background:linear-gradient(90deg,var(--blue-deep),var(--blue))}
.cta .wrap{display:flex;align-items:center;justify-content:space-between;height:191px;color:#fff}
.cta p{font-size:18px;font-weight:500}
.cta h3{font-family:"Montserrat",sans-serif;font-size:30px;font-weight:600;margin-top:6px}
.cta .btn{padding:14px 30px;font-size:14px}

/* footer */
.footer{height:318px;background:var(--footer);color:#c5c8cc;padding-top:46px}
.footer .wrap{display:flex}
.col h5{color:#fff;font-size:17px;font-weight:500}
.col .rule{width:40px;height:2px;background:var(--teal);margin:10px 0 22px}
.line{display:flex;gap:10px;font-size:12px;line-height:1.55;margin-bottom:10px}
.line svg{flex:none;margin-top:2px}
.col p{font-size:12px;line-height:1.55}
.subscribe{margin-top:14px;height:28px;border:1px solid #55595d;font-size:10px;padding:8px;color:#8a8e92}
.footer .btn{margin-top:10px;width:190px;padding:8px 0;font-size:12px}
.map{width:184px;height:166px;background:linear-gradient(135deg,#e9ede6,#cfd9cc)}
.bottom{height:48px;background:var(--footer-deep);color:#9ca0a4;font-size:11px}
.bottom .wrap{display:flex;align-items:center;justify-content:space-between;height:48px}
.socials{display:flex;gap:16px;align-items:center}
.socials i{width:10px;height:10px;background:#5d6164;display:block}
.to-top{width:30px;height:30px;background:var(--teal);display:flex;align-items:center;justify-content:center}
</style>
</head>
<body>

<div class="topbar"><div class="wrap"><span>30 Years Of Experience In Printed Circuit Boards</span><span>Login / Register &nbsp; | &nbsp; ENG</span></div></div>

<header class="header"><div class="wrap">
  <div class="brand"><span class="mark"></span>Kolrith</div>
  <div class="info">
    <svg width="18" height="24" viewBox="0 0 18 24"><path d="M9 0C4 0 0 4 0 9c0 7 9 15 9 15s9-8 9-15c0-5-4-9-9-9zm0 12a3 3 0 1 1 0-6 3 3 0 0 1 0 6z" fill="#0353a1"/></svg>
    <span>18/F, Harbour Crest<br>41 Marlow Road,<br>Wan Chai, HK</span>
  </div>
  <div class="info">
    <svg width="24" height="24" viewBox="0 0 24 24"><circle cx="12" cy="12" r="11" fill="none" stroke="#0353a1" stroke-width="2"/><path d="M6 8h12v8H6z M6 8l6 5 6-5" fill="none" stroke="#0353a1" stroke-width="1.5"/></svg>
    <span>sales@kolrithpanel.com</span>
  </div>
  <a class="btn">&#10003; &nbsp;Get A Quote</a>
</div></header>

<nav class="nav"><div class="wrap">
  <span class="active">HOME</span><span>PRODUCTS</span><span>OUR FACILITIES</span><span>CUSTOMERS</span><span>NEWS</span><span>QUOTES</span><span>CONTACT US</span>
  <span class="phone"><svg width="20" height="20" viewBox="0 0 24 24"><circle cx="12" cy="12" r="11" fill="none" stroke="#333a40" stroke-width="2"/><path d="M8 7l2 0 1 3-1.5 1a7 7 0 0 0 3.5 3.5l1-1.5 3 1v2c0 1-1 1.5-2 1.5C10 17 7 14 7 9c0-1 .5-2 1-2z" fill="#333a40"/></svg>(852) 2940 6618</span>
</div></nav>

<section class="hero" role="img" aria-label="Photograph of printed circuit boards on the production line">
  <div class="hero-title">Our <strong>Printed Circuit Board</strong> Business is Committed to <em>Excellence</em></div>
  <div class="appointment">
    <h3><svg width="18" height="18" viewBox="0 0 18 18"><rect x="1" y="3" width="16" height="14" fill="none" stroke="#fff" stroke-width="2"/><path d="M1 7h16M5 1v4M13 1v4" stroke="#fff" stroke-width="2"/></svg>Book An Appointment</h3>
    <form>
      <div class="field">NAME</div>
      <div class="field">EMAIL</div>
      <div class="field">PHONE</div>
      <div class="field area">MESSAGE</div>
      <div style="text-align:center"><span class="btn" style="width:230px;padding:8px 0">Submit</span></div>
    </form>
  </div>
</section>

<section class="features"><div class="wrap">
  <div class="feature"><svg width="30" height="30" viewBox="0 0 30 30"><circle cx="15" cy="15" r="13" fill="none" stroke="#fff" stroke-width="2"/><path d="M15 7v16M11 11h6a3 3 0 0 1 0 6h-4a3 3 0 0 0 0 6" fill="none" stroke="#fff" stroke-width="2"/></svg>Cost Competitiveness</div>
  <div class="feature"><svg width="30" height="30" viewBox="0 0 30 30"><path d="M2 24l9-9 6 5 11-12M22 8h6v6" fill="none" stroke="#fff" stroke-width="2.5"/></svg>Stable Financial Position</div>
  <div class="feature"><svg width="30" height="30" viewBox="0 0 30 30"><circle cx="15" cy="12" r="8" fill="none" stroke="#fff" stroke-width="2"/><path d="M11 20h8v6h-8z" fill="#fff"/></svg>Strong Management Experience</div>
  <div class="feature"><svg width="30" height="30" viewBox="0 0 30 30"><circle cx="15" cy="15" r="13" fill="none" stroke="#fff" stroke-width="2"/><circle cx="15" cy="15" r="5" fill="none" stroke="#fff" stroke-width="2"/><path d="M6 6l6 6M24 6l-6 6M6 24l6-6M24 24l-6-6" stroke="#fff" stroke-width="2"/></svg>Flexible Support</div>
</div></section>

<section class="who"><div class="wrap">
  <h2 class="section-title">Who <span>We Are</span></h2>
  <div class="divider"><i></i><b></b><i></i></div>
  <p class="intro">Established in 1987, Kolrith Global Limited (KGL) is a Hong Kong company specializing in single and double sided printed circuit boards. Its manufacturing facility is located in a self-owned facility in southern China, which is 90 minutes from Hong Kong.</p>
  <div class="cards">
    <div class="card filled"><h4>Our Mission</h4>Our mission is to become a premium low costs PCB supplier that fully embraces human, social and environmental responsibilities.</div>
    <div class="card"><h4>Our Capacity</h4>Through our insatiable drive to maximize efficiency, KGL is becoming a highly efficient PCB factory with a capacity of 140,000 square meter a month.</div>
    <div class="card"><h4>Our Vision</h4>PCB is our business and it is through continued automation and innovation that will drive our growth in the next 10 years.</div>
    <div class="card filled"><h4>Our Facility</h4>Maintaining a highly automated factory is the only way to ensure consistent product and long term competitive efficiency.</div>
  </div>
  <div class="photo" role="img" aria-label="Photograph of automated PCB processing machines in the factory"></div>
</div></section>

<section class="stats"><div class="wrap">
  <div class="stat"><svg width="44" height="44" viewBox="0 0 44 44"><circle cx="22" cy="14" r="8" fill="#fff"/><path d="M6 40c0-9 7-15 16-15s16 6 16 15z" fill="#fff"/></svg><b>100%</b><span>Privately Owned</span></div>
  <div class="stat"><svg width="44" height="44" viewBox="0 0 44 44"><circle cx="14" cy="16" r="6" fill="#fff"/><circle cx="30" cy="16" r="6" fill="#fff"/><path d="M2 38c0-8 5-13 12-13s12 5 12 13zM18 38c0-8 5-13 12-13s12 5 12 13z" fill="#fff"/></svg><b>132</b><span>Our Employees</span></div>
  <div class="stat"><svg width="44" height="44" viewBox="0 0 44 44"><path d="M4 40V22l10-6v6l10-6v6l10-6v24z" fill="#fff"/><path d="M34 8h6v32h-6z" fill="#fff"/></svg><b>130,000</b><span>Production Capacity (m²)</span></div>
</div></section>

<section class="products"><div class="wrap">
  <div class="center"><h2 class="section-title">Our <span>Products</span></h2><div class="divider"><i></i><b></b><i></i></div></div>
  <div class="tabs"><span class="on">Single Sided PCBs</span><span class="sep"></span><span>Double Sided / Multi Layered PCBs</span></div>
  <h3 class="product-head">Single Layered Printed Circuit Boards</h3><div class="rule"></div>
  <p class="product-desc">We are offering single layered circuit boards through our own production facility in China for customers in the following industries:</p>
  <div class="tables">
    <table style="width:306px">
      <tr><th colspan="2">&#9638; &nbsp;Application Percent %</th></tr>
      <tr><td>Household Appliances</td><td>40%</td></tr>
      <tr><td>Power Supply</td><td>10%</td></tr>
      <tr><td>Lighting Control System</td><td>20%</td></tr>
      <tr><td>Others</td><td>15%</td></tr>
    </table>
    <table style="width:350px">
      <tr><th colspan="2">&#9638; &nbsp;Raw Materials</th></tr>
      <tr><td>Paper Phenolic</td><td>XPC, FR-1 &amp; FR-2</td></tr>
      <tr><td>Paper Epoxy</td><td>CEM-1</td></tr>
      <tr><td>Glass Epoxy</td><td>CEM-3 &amp; FR-4</td></tr>
      <tr><td>Overall Thickness (T)</td><td>0.4mm – 1.6mm ± 0.13mm</td></tr>
    </table>
  </div>
  <a class="btn">&#10140; Read More</a>
</div></section>

<section class="testimonials">
  <h2 class="section-title">Testimonials</h2>
  <div class="divider"><i></i><b></b><i></i></div>
  <div class="avatars">
    <div class="avatar" role="img" aria-label="Customer portrait"></div>
    <div class="avatar" role="img" aria-label="Customer portrait"></div>
    <div class="avatar" role="img" aria-label="Customer portrait"></div>
    <div class="avatar" role="img" aria-label="Customer portrait"></div>
    <div class="avatar" role="img" aria-label="Customer portrait"></div>
  </div>
  <p class="quote">“ Duis aute irure dolor in reprehenderit in voluptate velit esse cillum dolore eu fugiat nulla pariatur. Excepteur sint occaecat cupidatat non proident sunt in culpa qui officia deserunt mollit anim id est laborum.</p>
  <p class="who-said">Marcus Hale <small>M.D.</small></p>
  <div class="dots"><i></i><i></i><i></i></div>
</section>

<section class="news"><div class="wrap">
  <div class="center"><h2 class="section-title">Latest <span>News</span></h2><div class="divider"><i></i><b></b><i></i></div></div>
  <div class="news-list">
    <article class="post"><div class="img" role="img" aria-label="Photograph of a worker inspecting boards"></div><div class="body"><h4>Nemo enim ipsam quia voluptas</h4><div class="meta">By admin | Feb 07, 2018 | No Comments</div><p>Neque porro quisquam est, qui dolorem ipsum quia dolor sit amet, consectetur adipisci velit sed quia non.</p><a>Read More</a></div></article>
    <article class="post"><div class="img" role="img" aria-label="Photograph of the production floor"></div><div class="body"><h4>Nemo enim ipsam quia voluptas</h4><div class="meta">By admin | Feb 07, 2018 | No Comments</div><p>Neque porro quisquam est, qui dolorem ipsum quia dolor sit amet, consectetur adipisci velit sed quia non.</p><a>Read More</a></div></article>
    <article class="post"><div class="img" role="img" aria-label="Photograph of PCB processing equipment"></div><div class="body"><h4>Nemo enim ipsam quia voluptas</h4><div class="meta">By admin | Feb 07, 2018 | No Comments</div><p>Neque porro quisquam est, qui dolorem ipsum quia dolor sit amet, consectetur adipisci velit sed quia non.</p><a>Read More</a></div></article>
  </div>
</div></section>

<section class="partners"><div class="wrap">
  <svg width="16" height="26" viewBox="0 0 16 26"><path d="M14 2L3 13l11 11" fill="none" stroke="#0353a1" stroke-width="3"/></svg>
  <div class="partner">Norvane</div><div class="partner">Keltrix</div><div class="partner">Ostberg</div><div class="partner">Brennel</div><div class="partner">Avelia</div><div class="partner">Quorra</div>
  <svg width="16" height="26" viewBox="0 0 16 26"><path d="M2 2l11 11L2 24" fill="none" stroke="#0353a1" stroke-width="3"/></svg>
</div></section>

<section class="cta"><div class="wrap">
  <div><p>Do You Have any Question?</p><h3>Feel Free To Request For a Quote</h3></div>
  <a class="btn">Request For Quote</a>
</div></section>

<footer class="footer"><div class="wrap">
  <div class="col" style="width:240px"><h5>Contact Us</h5><div class="rule"></div>
    <div class="line"><svg width="10" height="14" viewBox="0 0 18 24"><path d="M9 0C4 0 0 4 0 9c0 7 9 15 9 15s9-8 9-15c0-5-4-9-9-9z" fill="#00a990"/></svg><span>18/F, Harbour Crest<br>41 Marlow Road<br>Wan Chai, Hong Kong</span></div>
    <div class="line"><svg width="12" height="12" viewBox="0 0 12 12"><path d="M2 1h3l1 3-2 1a6 6 0 0 0 3 3l1-2 3 1v3c-6 0-9-3-9-9z" fill="#00a990"/></svg>+852-2940 6618</div>
    <div class="line"><svg width="12" height="12" viewBox="0 0 12 12"><rect x="1" y="1" width="10" height="10" fill="none" stroke="#00a990" stroke-width="1.5"/></svg>+852-2940 6619</div>
    <div class="line"><svg width="12" height="12" viewBox="0 0 12 12"><path d="M1 3h10v7H1zM1 3l5 4 5-4" fill="none" stroke="#00a990" stroke-width="1.3"/></svg>sales@kolrithpanel.com</div>
  </div>
  <div class="col" style="width:195px;padding-top:60px">
    <div class="line"><svg width="10" height="14" viewBox="0 0 18 24"><path d="M9 0C4 0 0 4 0 9c0 7 9 15 9 15s9-8 9-15c0-5-4-9-9-9z" fill="#00a990"/></svg><span>7 Linden Park Road<br>Eastgate Industrial Zone<br>Qingmu Town<br>Guangdong Province<br>China 510880</span></div>
    <div class="line"><svg width="12" height="12" viewBox="0 0 12 12"><path d="M2 1h3l1 3-2 1a6 6 0 0 0 3 3l1-2 3 1v3c-6 0-9-3-9-9z" fill="#00a990"/></svg>+86(769)</div>
    <div class="line"><svg width="12" height="12" viewBox="0 0 12 12"><rect x="1" y="1" width="10" height="10" fill="none" stroke="#00a990" stroke-width="1.5"/></svg>+86(769)8215 4470</div>
  </div>
  <div class="col" style="width:218px"><h5>Newsletter</h5><div class="rule"></div>
    <p>Subscribe to our newsletter for latest updates</p>
    <div class="subscribe">Email</div>
    <span class="btn" style="display:block;width:190px;padding:8px 0;font-size:12px;margin-top:10px">Subscribe</span>
  </div>
  <div class="col"><h5>Locate Us</h5><div class="rule"></div>
    <div class="map" role="img" aria-label="Map showing the office location"></div>
  </div>
</div></footer>

<div class="bottom"><div class="wrap">
  <span>©Copyright Kolrith Global Limited</span>
  <div class="socials"><i></i><i></i><i></i><span class="to-top"><svg width="12" height="8" viewBox="0 0 12 8"><path d="M1 7l5-5 5 5" fill="none" stroke="#fff" stroke-width="2"/></svg></span></div>
</div></div>

</body>
</html>
```